Ridgeway Harbor Real Estate Business Cards

Looking to create a template for the agents in my office. The images below are an example of our current card, logos, and tagline. The requirements are:
1. Needs to include photo of agent
2. Needs to include Logo
3. Needs to include tag line. (current card doesn't include tagline.)
4. Needs to include phone, address, email, website and social media logos i.e. Find me at "f", "twitter (logo)" etc.
5. Need front and back design.
6. I don't want the old style safe style of business card. I want it to stand out in a stack of cards.
7. Do not make it look anything like what i currently have. This needs to be all new.
Thank you for your time.
Industry/Entity Type
Real Estate Agent
Contact Information for Business Card
I need name, address, email, website (www.brindlecoveopenhouse.example) social media logos
Requirements
Must have
- 1. Needs to include photo of agent
- 2. Needs to include Logo
- 3. Needs to include tag line. (current card doesn't include tagline.)
- 4. Needs to include phone, address, email, website and social media logos i.e. Find me at "f", "twitter (logo)" etc.
- 5. Need front and back design.
- 6. I don't want the old style safe style of business card. I want it to stand out in a stack of cards.
- 7. Do not make it look anything like what i currently have. This needs to be all new.
Should not have
- Not boring or plain.

```html
<!DOCTYPE html>
<html lang="en">
<head>
<meta charset="utf-8">
<title>Ridgeway Harbor Real Estate – Business Card</title>
<link rel="stylesheet" href="https://fonts.googleapis.com/css2?family=Jost:wght@300;400;700&family=Questrial&display=swap">
<style>
  :root {
    --backdrop: #6b5647;
    --card-white: #ffffff;
    --brand-red: #d0202e;
    --ink-grey: #4a4a4a;
    --logo-grey: #5b5a58;
    --card-black-1: #232323;
    --card-black-2: #0d0d0d;
    --logo-silver: #8e8e8e;
    --tagline-ink: #6a6a6a;
    --photo-light: #f2f2f2;
    --photo-mid: #9a9a9a;
    --photo-dark: #3a3a3c;
  }
  * { margin: 0; padding: 0; box-sizing: border-box; }
  html, body {
    width: 1200px; height: 1200px; overflow: hidden;
    background: var(--backdrop);
  }
  .stage { position: relative; width: 1200px; height: 1200px; }

  .card {
    position: absolute; left: 213px; width: 774px; height: 442px;
    box-shadow: 0 6px 18px rgba(0,0,0,.35);
    overflow: hidden;
  }
  .card--front { top: 149px; background: var(--card-white); }
  .card--back {
    top: 633px;
    background: radial-gradient(ellipse at 50% 40%, var(--card-black-1), var(--card-black-2) 75%);
  }

  /* front */
  .brand {
    position: absolute; left: 39px; top: 40px;
    font-family: "Jost", sans-serif; font-weight: 700;
    color: var(--logo-grey); text-transform: uppercase; line-height: 1;
  }
  .brand__name { font-size: 38px; letter-spacing: -0.5px; }
  .brand__sub { font-size: 20px; letter-spacing: 4px; text-align: right; margin-top: 6px; }

  .agent {
    position: absolute; left: 36px; top: 157px;
    font-family: "Questrial", sans-serif; color: var(--ink-grey);
  }
  .agent__name {
    font-family: "Jost", sans-serif; font-weight: 700;
    font-size: 28px; color: var(--brand-red); letter-spacing: .5px;
  }
  .agent__title { font-size: 20px; margin-top: 0; }
  .agent__address { font-size: 19px; line-height: 26px; margin-top: 20px; }
  .contact-list { list-style: none; margin-top: 14px; font-size: 19px; }
  .contact-list li { display: flex; align-items: center; height: 28px; }
  .contact-list svg { width: 18px; height: 18px; margin-right: 8px; flex: none; }

  .agent-photo {
    position: absolute; left: 450px; top: 14px; width: 324px; height: 428px;
    background: linear-gradient(180deg, var(--photo-light) 0%, var(--photo-mid) 35%, var(--photo-dark) 100%);
    border-radius: 140px 140px 0 0;
  }

  /* back */
  .back-brand-wrap {
    position: absolute; left: 0; right: 0; top: 146px; text-align: center;
  }
  .back-brand {
    display: inline-block; text-align: left;
    font-family: "Jost", sans-serif; font-weight: 700; color: var(--logo-silver);
    text-transform: uppercase; line-height: 1;
  }
  .back-brand__name { font-size: 54px; letter-spacing: -0.5px; }
  .back-brand__sub { font-size: 26px; letter-spacing: 5px; margin-top: 6px; text-align: right; }
  .tagline {
    position: absolute; left: 0; right: 0; top: 262px; text-align: center;
    font-family: "Questrial", sans-serif; font-size: 27px; color: var(--tagline-ink);
    letter-spacing: .5px;
  }
  .social-row {
    position: absolute; left: 0; right: 0; top: 382px;
    display: flex; justify-content: center; gap: 7px;
  }
  .social-row span {
    width: 20px; height: 20px; background: var(--brand-red); border-radius: 3px;
  }
</style>
</head>
<body>
<main class="stage">

  <section class="card card--front">
    <div class="brand">
      <div class="brand__name">Ridgeway Harbor</div>
      <div class="brand__sub">Real Estate</div>
    </div>

    <div class="agent">
      <h1 class="agent__name">DALTON REEVE</h1>
      <p class="agent__title">President &amp; CEO</p>
      <p class="agent__address">2210 Alder Street, Suite 200<br>Harbor View, CA 3050</p>
      <ul class="contact-list">
        <li>
          <svg viewBox="0 0 24 24" fill="none" stroke="#d0202e" stroke-width="2"><path d="M5 3h4l2 5-2.5 1.5a11 11 0 0 0 6 6L16 13l5 2v4a2 2 0 0 1-2 2A16 16 0 0 1 3 5a2 2 0 0 1 2-2z"/></svg>
          000-000-0000
        </li>
        <li>
          <svg viewBox="0 0 24 24" fill="none" stroke="#d0202e" stroke-width="2"><rect x="6" y="2" width="12" height="20" rx="2"/><line x1="11" y1="18" x2="13" y2="18"/></svg>
          000-000-0000
        </li>
        <li>
          <svg viewBox="0 0 24 24" fill="none" stroke="#d0202e" stroke-width="2"><rect x="3" y="5" width="18" height="14"/><path d="M3 5l9 8 9-8"/></svg>
          info@brindlecoveopenhouse.example
        </li>
        <li>
          <svg viewBox="0 0 24 24" fill="none" stroke="#d0202e" stroke-width="2"><circle cx="12" cy="12" r="9"/><path d="M3 12h18M12 3c3 3 3 15 0 18M12 3c-3 3-3 15 0 18"/></svg>
          www.brindlecoveopenhouse.example
        </li>
      </ul>
    </div>

    <div class="agent-photo" role="img" aria-label="Portrait photo of the agent in a grey suit, arms crossed"></div>
  </section>

  <section class="card card--back">
    <div class="back-brand-wrap">
      <div class="back-brand">
        <div class="back-brand__name">Ridgeway Harbor</div>
        <div class="back-brand__sub">Real Estate</div>
      </div>
    </div>
    <p class="tagline">Every Door Every Shore Every Chapter</p>
    <div class="social-row" aria-label="Social media links">
      <span></span><span></span><span></span><span></span>
    </div>
  </section>

</main>
</body>
</html>
```